Tobin's Jewelry Studio Needs a Moving Location Flyer

We need a flyer to inform our customers of our location moving. We will be moving to our city's downtown which is only 1 mile away from our current address. We will be having a moving sale ( Up to 80% off). The sale starts Sept. 8th Our business creates, sells, and repairs fine jewelry. Dimensions are 5"x8"

Target Market(s)

Women ages 25-55

Industry/Entity Type

Jewelry

Colors
85abd2
cfdeed

Requirements
Must have
• Our logo
• Mention of the sale
• Our current address
• 4785 Cresthaven Blvd.
• Dunmore, Ca 94318
• (415)826-3319
Nice to have
• Mention that we're relocating to downtown Dunmore (new location opening Nov. 1st.)

```html
<!DOCTYPE html>
<html lang="en">
<head>
<meta charset="utf-8">
<title>Tobin's Jewelry Studio – We're Moving</title>
<link href="https://fonts.googleapis.com/css2?family=Oswald:wght@400;500;700&family=Libre+Baskerville:wght@400;700&family=Yellowtail&family=Quicksand:wght@500&display=swap" rel="stylesheet">
<style>
  :root {
    --brand-blue: #85abd2;
    --sky-blue: #8db1d8;
    --pale-blue: #cfdeed;
    --aqua: #c6e5ec;
    --band-gray: #c8c8c8;
    --cocoa: #4a2a1f;
    --sale-red: #b3211e;
    --frame-red: #9a2b2b;
    --white: #ffffff;
  }
  * { margin: 0; padding: 0; box-sizing: border-box; }
  html, body { width: 750px; height: 1200px; overflow: hidden; background: var(--white); }
  .flyer { position: relative; width: 750px; height: 1200px; overflow: hidden; background: var(--aqua); }

  .brand-band { position: absolute; left: 0; top: 0; width: 750px; height: 198px; background: var(--sky-blue); }
  .brand { position: absolute; left: 0; top: 60px; width: 750px; display: flex; align-items: center; justify-content: center; gap: 22px; }
  .brand-rule { width: 90px; height: 3px; background: var(--cocoa); }
  .brand-dot { width: 22px; height: 22px; border-radius: 50%; background: var(--pale-blue); }
  .brand-name { font-family: "Quicksand", sans-serif; font-weight: 500; font-size: 42px; color: var(--white); letter-spacing: 1px; }

  .headline-band { position: absolute; left: 0; top: 206px; width: 750px; height: 146px; background: linear-gradient(180deg, #cfcfcf, var(--band-gray)); }
  .headline { position: absolute; left: 0; top: 222px; width: 750px; text-align: center; font-family: "Oswald", sans-serif; font-weight: 700; font-size: 98px; line-height: 1.1; color: var(--cocoa); transform: skewX(-10deg); letter-spacing: 1px; }

  .divider { position: absolute; left: 0; width: 750px; }
  .divider-white-a { top: 352px; height: 10px; background: var(--white); }
  .divider-blue { top: 362px; height: 6px; background: var(--pale-blue); }
  .divider-white-b { top: 368px; height: 10px; background: var(--white); }

  .relocating { position: absolute; left: 0; top: 474px; width: 750px; text-align: center; font-family: "Libre Baskerville", serif; font-weight: 700; font-size: 30px; color: var(--cocoa); }

  .sale-art { position: absolute; left: 0; top: 520px; width: 750px; height: 630px; }
  .sale-art text { font-family: "Oswald", sans-serif; }

  .footer-band { position: absolute; left: 0; top: 1150px; width: 750px; height: 50px; background: var(--brand-blue); }
  .footer-city { display: block; text-align: center; line-height: 50px; font-family: "Libre Baskerville", serif; font-size: 24px; color: var(--white); }
</style>
</head>
<body>
<main class="flyer">
  <header class="brand-band">
    <div class="brand">
      <span class="brand-rule"></span>
      <span class="brand-dot"></span>
      <span class="brand-name">Tobin's Jewelry Studio</span>
      <span class="brand-rule"></span>
    </div>
  </header>

  <section class="headline-band"></section>
  <h1 class="headline">WE'RE MOVING!</h1>

  <div class="divider divider-white-a"></div>
  <div class="divider divider-blue"></div>
  <div class="divider divider-white-b"></div>

  <p class="relocating">Relocating to Downtown Dunmore</p>

  <svg class="sale-art" viewBox="0 520 750 630" xmlns="http://www.w3.org/2000/svg">
    <g class="opening-line" font-weight="700" font-size="72">
      <text x="94" y="592" textLength="330" lengthAdjust="spacingAndGlyphs" fill="var(--white)" stroke="var(--brand-blue)" stroke-width="3">OPENING</text>
      <text x="448" y="592" textLength="210" lengthAdjust="spacingAndGlyphs" fill="var(--brand-blue)">NOV 1ST</text>
    </g>

    <g class="sale-frame" fill="none" stroke="var(--frame-red)" stroke-width="4">
      <path d="M70 700 H245 Q245 664 270 664 H480 Q505 664 505 700 H680 Q680 716 702 716 V1112 Q680 1112 680 1134 H70 Q70 1112 48 1112 V716 Q70 716 70 700 Z"/>
      <path d="M78 708 H253 Q253 672 278 672 H472 Q497 672 497 708 H672 Q672 724 694 724 V1104 Q672 1104 672 1126 H78 Q78 1104 56 1104 V724 Q78 724 78 708 Z" stroke-width="2"/>
    </g>

    <text class="sale-date" x="375" y="703" text-anchor="middle" font-weight="500" font-size="40" fill="var(--cocoa)">SEPT 8TH</text>

    <rect class="sale-panel" x="62" y="720" width="626" height="346" fill="var(--brand-blue)" stroke="var(--cocoa)" stroke-width="3"/>

    <g class="sale-offer" font-weight="700">
      <text x="92" y="858" font-size="130" textLength="135" lengthAdjust="spacingAndGlyphs" fill="var(--cocoa)">UP</text>
      <text x="92" y="990" font-size="130" textLength="135" lengthAdjust="spacingAndGlyphs" fill="var(--cocoa)">TO</text>
      <text x="244" y="1050" font-size="400" textLength="290" lengthAdjust="spacingAndGlyphs" fill="var(--sale-red)">80</text>
      <text x="548" y="900" font-size="190" textLength="118" lengthAdjust="spacingAndGlyphs" fill="var(--cocoa)">%</text>
      <text x="546" y="1010" font-family="Yellowtail, cursive" font-weight="400" font-size="96" fill="var(--sale-red)">off!</text>
    </g>

    <g class="sale-contact" font-size="32" font-weight="400" fill="var(--cocoa)">
      <text x="105" y="1115">(415)826-3319</text>
      <path d="M318 1093 l9 9 -9 9 -9 -9 Z" fill="var(--sale-red)"/>
      <text x="340" y="1115">4785 Cresthaven Blvd.</text>
    </g>
  </svg>

  <footer class="footer-band">
    <span class="footer-city">Dunmore, CA 94318</span>
  </footer>
</main>
</body>
</html>
```